Kavoni. Sunless Tanning Mousse Label

I'm looking for a label creation for a new brand of sunless tanning solutions. They are in 6.7oz bottles (template attached).

For the front of the bottle (see template) I would like an abstract multi coloured design taking up just over half the top of the bottle (approx 60%) and going around the design (this is similar to the design inspiration attached). I would this design to use the attached colour palette of pinks. It can be swirls, drips, squares, lines, whatever you think will look good.

The logo will then be over top of that abstract design in the upper 1/3, in the colour #3fe0d0

Under the abstract design the following text:

Wild Plume (Larger text)
Coral Drift (2nd heading)
1 Hour Sunless Mousse (Sub text)
The No Orange Guarantee! (Sub text)
Vegan Formula (sub text)

The sub texts for above can be fun, have coloured background, different fonts, whatever looks good and is sill fun.

Towards the bottom of the front of bottle we require the sizing information:

200ml 6.7 Fl Oz

On the left side of the front (so in the template the middle smaller section) I would like the phrase "You ain't gotta get ready if you stay ready" Could you please make this as a separate little quote, with a fun design to it. It's like a little hidden gem on the side of the bottle.

On the back of the bottle for now can you please start towards the top with:

Wild Plume Mousse (larger)
Coral drift (second heading)
Deep Mediterranean Inspired Tan (second heading)
Easy to Apply & Streak Free
Vegan friendly & 100% natural DHA tan actives

Under this I require approx 1.5" of Lorem Ipsum for now which will take the place of directions for using the product.

Under that in small writing can we include "Warning: This product does not contain a sunscreen and will not protect against sunburn. For external use only. If skin irritation occurs, discontinue use. Carry out a patch test 24 hours prior to full body use. Store below 25(degrees sign)C."

At the bottom is the smallest yet still legible writing, can we include the ingredients that are listed below.

Target Market(s)

Females 24-35 who take care of themselves and always want to look good. It's a youthful fun product.

Requirements
Must have
• Bright colours, and just screams FUN and youthful.

Ingredients must be listed on the back. They dont' need to take up more than an inch in height, less if possible.
*******************************************

INGREDIENTS: Water (Aqua), Propylene Glycol, Dihydroxyacetone, Peg-6 Caprylic/Capric Glycerides, Dihydroxypropyl Peg-5 Linoleammonium Chloride, Peg-7 Glyceryl Cocoate, Caramel,
Phenoxyethanol, Caprylyl Glycol, Potassium Sorbate, Hexylene Glycol, Glycerin, Helianthus Annuus (Sunflower) Seed Oil, Beta Vulgaris (Beet) Root Extract, Panthenol, Solanum Lycopersicum
(Tomato) Fruit Extract, Vaccinium Macrocarpon (Cranberry) Fruit Extract, L-ascorbic Acid (Vitamin C), Tocopheryl Acetate (Vitamin E), Theobroma Cacao (Cocoa) Seed Butter, Rosa Canina (Rose Hip)
Fruit Oil, Glycine Soja (Soybean) Oil, Cucumis Sativus (Cucumber) Fruit Extract, Blue 1 (CI 42090), Red 40 (CI 16035), Yellow 6 (CI 15985), Green 5 (CI 61570), Yellow 5 (CI 19140), Red 33 (CI 17200)

*****************************
Nice to have
• Several options to choose from, some can include a gradient into geometric shapes, rather than solid colour. Experiment
Should not have
• Do not want it to look medical.
Want colours to stay in the same pink family for the abstract design - can use white also.

```html
<!DOCTYPE html>
<html lang="en">
<head>
<meta charset="utf-8">
<title>Kavoni – Wild Plume Mousse Label</title>
<link href="https://fonts.googleapis.com/css2?family=Montserrat:wght@400;500;600;700;800&family=Yellowtail&display=swap" rel="stylesheet">
<style>
  :root {
    --pink: #e8198b;
    --pink-light: #f37cbb;
    --pink-deep: #d10f7c;
    --teal: #45d3c4;
    --plum: #a3157f;
    --ink: #1d1d1b;
    --sun: #f7e51a;
    --white: #ffffff;
    --page: #ffffff;
  }
  * { box-sizing: border-box; margin: 0; padding: 0; }
  html, body { width: 800px; height: 1200px; overflow: hidden; background: var(--page); }
  body { font-family: "Montserrat", Arial, sans-serif; position: relative; }

  .label-frame {
    position: absolute; left: 20px; top: 284px;
    width: 760px; height: 632px;
    box-shadow: 0 6px 24px rgba(0,0,0,.18);
    overflow: hidden;
  }
  .label {
    position: absolute; left: 0; top: 0;
    width: 905px; height: 752px;
    transform: scale(0.8398); transform-origin: 0 0;
    background: var(--white);
  }
  .label-art { position: absolute; inset: 0; width: 905px; height: 752px; }

  /* back panel */
  .back { position: absolute; left: 52px; width: 280px; text-align: center; color: var(--white); }
  .back-title { top: 38px; }
  .back-name { font-weight: 800; font-size: 29px; letter-spacing: .5px; line-height: 1; }
  .back-type { font-weight: 500; font-size: 30px; letter-spacing: 7px; color: var(--teal); line-height: 1.1; margin-top: 2px; }
  .back-shade { margin-top: 22px; font-weight: 700; font-size: 16px; letter-spacing: 4px; display: flex; align-items: center; justify-content: center; gap: 6px; }
  .back-shade::before, .back-shade::after { content: ""; width: 20px; height: 2px; background: var(--white); }
  .back-tan { margin-top: 20px; font-weight: 700; font-size: 16px; color: var(--teal); line-height: 1.25; }
  .back-claims { margin-top: 16px; font-size: 13px; line-height: 1.2; }
  .back-claims strong { font-weight: 700; }
  .back-directions { top: 292px; font-size: 13.5px; line-height: 1.17; }

  .warning { position: absolute; left: 62px; top: 514px; width: 260px; text-align: center; color: var(--ink); font-size: 10.4px; line-height: 1.2; }
  .warning-head { display: flex; justify-content: center; align-items: center; gap: 5px; color: var(--pink); font-weight: 600; font-size: 9px; margin-bottom: 6px; }
  .ingredients { position: absolute; left: 60px; top: 616px; width: 266px; text-align: center; color: var(--ink); font-size: 6.2px; line-height: 1.3; }
  .ingredients strong { font-weight: 800; }

  /* side quote */
  .quote { position: absolute; left: 378px; top: 40px; width: 90px; height: 340px; }
  .quote-main { position: absolute; left: 0; bottom: 0; transform: rotate(-90deg); transform-origin: 0 0; top: 338px;
    white-space: nowrap; font-weight: 700; font-size: 18.5px; color: var(--white); letter-spacing: .3px; }
  .quote-script { position: absolute; left: 24px; top: 330px; transform: rotate(-90deg); transform-origin: 0 0;
    white-space: nowrap; font-family: "Yellowtail", cursive; font-size: 46px; color: var(--sun); line-height: 1; }

  /* front panel */
  .brand { position: absolute; left: 514px; top: 86px; display: flex; align-items: flex-end; gap: 8px; }
  .brand-name { font-weight: 700; font-size: 72px; color: var(--white); letter-spacing: 1px; line-height: 1; }
  .brand-dot { width: 14px; height: 14px; border-radius: 50%; background: var(--white); margin-bottom: 8px; }

  .front { position: absolute; left: 514px; }
  .front-name-top { top: 456px; font-weight: 700; font-size: 60px; color: var(--ink); line-height: 1; letter-spacing: -1px; }
  .front-name-main { top: 514px; font-weight: 700; font-size: 68px; color: var(--pink); line-height: 1; letter-spacing: -1px; }
  .front-shade { top: 594px; font-weight: 600; font-size: 33px; color: var(--plum); letter-spacing: .5px; }
  .front-time { top: 634px; font-weight: 600; font-size: 15.5px; color: var(--plum); }
  .front-guarantee { top: 672px; font-weight: 400; font-size: 14px; color: var(--pink); }
  .front-vegan { top: 708px; display: flex; align-items: center; gap: 5px; font-size: 13px; color: var(--teal); font-weight: 500; }

  .size-badge { position: absolute; left: 822px; top: 667px; width: 54px; height: 54px; border-radius: 50%;
    background: var(--pink); color: var(--white); display: flex; flex-direction: column; align-items: center; justify-content: center; line-height: 1; }
  .size-badge .ml { font-weight: 700; font-size: 14px; }
  .size-badge .oz { font-size: 8.5px; margin-top: 1px; }
</style>
</head>
<body>
  <div class="label-frame">
    <div class="label">
      <svg class="label-art" viewBox="0 0 905 752" xmlns="http://www.w3.org/2000/svg">
        <defs>
          <radialGradient id="patternTone" cx="50%" cy="40%" r="75%">
            <stop offset="0" stop-color="#f25aa9"/>
            <stop offset="1" stop-color="#e11c88"/>
          </radialGradient>
        </defs>
        <path role="img" aria-label="Pink concentric circle pattern" fill="url(#patternTone)"
          d="M0 0 H905 V440 C860 450 830 410 790 420 C740 432 720 392 660 392
             C600 392 560 400 530 430 C500 462 470 530 430 535 C392 540 385 470 350 440
             C320 414 290 400 250 402 C200 405 160 418 110 410 C70 404 40 400 0 412 Z"/>
        <circle cx="320" cy="412" r="20" fill="#ee4aa0"/>
        <circle cx="320" cy="412" r="10" fill="#f9a8d2"/>
        <circle cx="570" cy="425" r="20" fill="#e8198b"/>
        <circle cx="695" cy="405" r="12" fill="#ffffff"/>
        <circle cx="792" cy="490" r="12" fill="#ee4aa0"/>
      </svg>

      <div class="back back-title">
        <div class="back-name">WILD PLUME</div>
        <div class="back-type">MOUSSE</div>
        <div class="back-shade">CORAL DRIFT</div>
        <div class="back-tan">DEEP MEDITERRANEAN<br>INSPIRED TAN</div>
        <p class="back-claims"><strong>Easy to Apply &amp; Streak Free</strong><br>Vegan friendly &amp; 100% natural<br>DHA tan actives</p>
      </div>
      <p class="back back-directions">Lorem ipsum dolor sit amet,<br>consectetuer adipiscing elit, sed diam<br>nonummy nibh euismod tincidunt ut<br>laoreet dolore magna.</p>

      <div class="quote">
        <span class="quote-main">YOU AIN'T GOTTA GET READY</span>
        <span class="quote-script">if you stay ready</span>
      </div>

      <div class="brand">
        <span class="brand-name">KAVONI</span>
        <span class="brand-dot"></span>
      </div>

      <div class="warning">
        <div class="warning-head">
          <svg width="14" height="12" viewBox="0 0 14 12"><path d="M7 1 L13 11 H1 Z" fill="none" stroke="currentColor" stroke-width="1.2"/><path d="M7 4.5 V7.8 M7 9 V9.8" stroke="currentColor" stroke-width="1.2"/></svg>
          WARNING
        </div>
        <p>This product does not contain a sunscreen and will not protect against sunburn. For external use only. If skin irritation occurs, discontinue use. Carry out a patch test 24 hours prior to full body use. Store below 25°C.</p>
      </div>

      <p class="ingredients"><strong>INGREDIENTS:</strong> Water (Aqua), Propylene Glycol, Dihydroxyacetone, Peg-6 Caprylic/Capric Glycerides, Dihydroxypropyl Peg-5 Linoleammonium Chloride, Peg-7 Glyceryl Cocoate, Caramel, Phenoxyethanol, Caprylyl Glycol, Potassium Sorbate, Hexylene Glycol, Glycerin, Helianthus Annuus (Sunflower) Seed Oil, Beta Vulgaris (Beet) Root Extract, Panthenol, Solanum Lycopersicum (Tomato) Fruit Extract, Vaccinium Macrocarpon (Cranberry) Fruit Extract, L-ascorbic Acid (Vitamin C), Tocopheryl Acetate (Vitamin E), Theobroma Cacao (Cocoa) Seed Butter, Rosa Canina (Rose Hip) Fruit Oil, Glycine Soja (Soybean) Oil, Cucumis Sativus (Cucumber) Fruit Extract, Blue 1 (CI 42090), Red 40 (CI 16035), Yellow 6 (CI 15985), Green 5 (CI 61570), Yellow 5 (CI 19140), Red 33 (CI 17200)</p>

      <div class="front front-name-top">WILD</div>
      <div class="front front-name-main">PLUME</div>
      <div class="front front-shade">CORAL DRIFT</div>
      <div class="front front-time">1 Hour Sunless Mousse</div>
      <div class="front front-guarantee">THE NO ORANGE GUARANTEE!</div>
      <div class="front front-vegan">
        <svg width="20" height="20" viewBox="0 0 20 20"><circle cx="10" cy="10" r="9.5" fill="var(--teal)"/><path d="M6 14 C7 8 10 6 15 5 C14 10 11 13 6 14 Z M6 14 L11 9" fill="#fff" stroke="var(--teal)" stroke-width=".8"/></svg>
        Vegan Formula
      </div>

      <div class="size-badge"><span class="ml">200ml</span><span class="oz">6.7 Fl Oz</span></div>
    </div>
  </div>
</body>
</html>
```